Revamp of our Premium Travel Website - BIG OPPORTUNITY -

This is our website's home page: www.velmoratrailsandvoyages.example
We have already started a redesign, please see attached. Base on the content and info attached, please propose a new redesign which is much better and looks super premium.
We are looking for someone to hire to redesign 2 full websites.
Please change compass for logo attached. change logo as needed.
YOU HAVE THE FREEDOM TO CHANGE EVERYTHING TO MAKE IT LOOK PREMIUM AND GREAT!

Target Market(s)

United States

Number of Pages Required

1 page

Colors

Designer to choose colors to be used in the design.

Requirements
Must have
• Must look premium and unique.
• Must be responsive with mobile, tablet, and desktop.
Nice to have
• Color pallete that looks premium. It should include gold color. You can change completely the colors provided in the sample.
• Change all fonts, and logo as needed.

```html
<!DOCTYPE html>
<html lang="en">
<head>
<meta charset="utf-8">
<title>Velmora Trails &amp; Voyages</title>
<link rel="stylesheet" href="https://fonts.googleapis.com/css2?family=Montserrat:wght@400;600;700;800&family=Open+Sans:ital,wght@0,400;0,600;0,700;1,400&display=swap">
<style>
:root{
  --gold:#f2c200;
  --gold-deep:#d9a400;
  --olive:#8da51c;
  --olive-dark:#6f8514;
  --teal:#2fb8c8;
  --ink:#1d1d1d;
  --text:#444;
  --muted:#888;
  --line:#e3e3e3;
  --pale-teal:#e6f8f9;
  --black:#0d0d0d;
  --white:#fff;
}
*{box-sizing:border-box;margin:0;padding:0}
html,body{width:1200px;height:5217px;overflow:hidden}
body{font-family:"Open Sans",Arial,sans-serif;color:var(--text);background:var(--white);position:relative;font-size:13px}
h1,h2,h3,h4{font-family:"Montserrat",Arial,sans-serif;color:var(--ink)}
.btn{display:inline-block;white-space:nowrap;background:var(--olive);color:var(--white);font-family:"Montserrat",Arial,sans-serif;font-weight:700;font-size:10px;letter-spacing:.5px;text-transform:uppercase;border-radius:14px;padding:8px 18px}

/* header & hero */
.hero{position:absolute;left:0;top:0;width:1200px;height:440px;
  background:
    radial-gradient(ellipse 420px 120px at 760px 175px,rgba(255,255,255,.85),rgba(255,255,255,0) 70%),
    radial-gradient(ellipse 520px 150px at 330px 215px,rgba(236,242,246,.75),rgba(236,242,246,0) 70%),
    linear-gradient(180deg,#6d95bd 0%,#a9c3d9 26%,#d7e2ea 40%,#8d9aa6 52%,#5f7a62 64%,#3c5a34 80%,#253c22 100%)}
.topbar{position:absolute;left:0;top:0;width:1200px;height:58px;background:rgba(0,0,0,.55);display:flex;align-items:center;padding:0 40px;white-space:nowrap}
.brand{display:flex;align-items:center;gap:10px;font-family:"Montserrat",sans-serif;font-weight:800;font-size:13px;color:var(--gold);letter-spacing:.4px;text-transform:uppercase}
.brand-dot{width:34px;height:34px;border-radius:50%;background:var(--gold);flex:none}
.nav{display:flex;gap:20px;margin-left:26px}
.nav a{color:var(--white);font-size:11px;font-weight:600;text-decoration:none;font-family:"Montserrat",sans-serif}
.nav a.active{color:var(--gold)}
.contact-mini{margin-left:auto;color:var(--white);font-size:9px;line-height:1.4}
.contact-mini b{font-size:13px;display:flex;align-items:center;gap:5px}
.topbar .btn{margin-left:14px;font-size:9px;padding:8px 14px}
.lang{color:var(--white);font-size:11px;margin-left:12px;font-weight:600}

/* memories */
.memories{position:absolute;top:440px;left:0;width:1200px;height:460px;background:var(--white)}
.section-title{text-align:center;font-weight:800;font-size:22px;text-transform:uppercase;line-height:1.35;color:var(--ink)}
.memories .section-title{margin-top:66px}
.mem-cards{display:flex;gap:22px;position:absolute;left:160px;top:170px}
.mem-card{width:200px;height:210px;border:1px solid var(--line);border-radius:6px;padding:18px 16px;box-shadow:0 3px 10px rgba(0,0,0,.08);background:var(--white)}
.mem-card.hl{background:var(--pale-teal)}
.mem-icon{width:38px;height:38px;border-radius:50%;background:var(--gold);margin-bottom:10px}
.mem-card h3{font-size:13px;font-weight:700;line-height:1.3;margin-bottom:8px}
.mem-card p{font-size:9.5px;color:var(--muted);line-height:1.45;font-style:italic}
.mem-card .by{font-size:9.5px;color:var(--ink);margin-top:8px;font-weight:600}

/* destination chooser */
.chooser{position:absolute;top:900px;left:0;width:1200px;height:1060px;background:linear-gradient(180deg,#34c3d2 0%,#27b2c6 55%,#3fb9c4 75%,#6bc8c6 100%)}
.chooser .section-title{color:var(--white);margin-top:50px}
.form-bar{position:absolute;left:160px;top:255px;width:880px;height:82px;background:var(--gold);border-radius:4px;display:flex;align-items:center;gap:14px;padding:0 22px;box-shadow:0 6px 14px rgba(0,0,0,.2)}
.field{flex:1;height:38px;background:var(--white);border-radius:3px;display:flex;align-items:center;gap:8px;padding:0 12px;font-size:10px;font-weight:700;color:var(--ink);text-transform:uppercase;font-family:"Montserrat",sans-serif;white-space:nowrap}
.chooser .cta{position:absolute;left:50%;transform:translateX(-50%);top:378px}
.dest-grid{position:absolute;left:160px;top:432px;width:880px;display:grid;grid-template-columns:repeat(4,205px);gap:20px}
.dest{height:240px;background:var(--white);border-radius:6px;overflow:hidden;box-shadow:0 4px 12px rgba(0,0,0,.18)}
.dest .ph{height:190px;position:relative}
.dest .info{position:absolute;right:8px;bottom:6px;background:rgba(0,0,0,.55);color:var(--white);font-size:8px;font-weight:700;padding:2px 6px;border-radius:3px}
.dest .name{height:50px;display:flex;align-items:center;justify-content:center;gap:6px;font-size:12px;font-weight:600;color:var(--ink)}
.check{width:13px;height:13px;border:1px solid var(--ink);display:inline-flex;align-items:center;justify-content:center}
.lake{position:absolute;left:0;top:860px;width:1200px;height:200px;background:linear-gradient(180deg,rgba(80,190,200,0) 0%,#6fc7c8 50%,#9fd6d2 100%)}

/* reviews */
.reviews{position:absolute;top:1960px;left:0;width:1200px;height:750px;background:linear-gradient(180deg,#fff 0%,#fff 85%,#eaf3f5 100%)}
.reviews .section-title{margin-top:22px}
.subtitle{text-align:center;font-size:12px;color:var(--muted);margin-top:6px}
.testi{position:absolute;left:160px;top:100px;width:880px;height:405px;background:var(--white);box-shadow:0 4px 14px rgba(0,0,0,.12);display:flex}
.testi-photo{width:452px;height:405px;background:
  radial-gradient(ellipse 200px 90px at 220px 250px,rgba(214,70,52,.9),rgba(214,70,52,0) 75%),
  linear-gradient(170deg,#e3ebf0 0%,#b9c6d0 30%,#7d8f9b 50%,#5b7a86 70%,#4c6a50 100%)}
.testi-body{flex:1;background:var(--pale-teal);padding:34px 30px}
.testi-body h4{font-size:14px;font-weight:700;line-height:1.4;margin-bottom:14px}
.testi-body p{font-size:11px;font-style:italic;color:var(--text);line-height:1.6;margin-bottom:10px}
.testi-body .visited{font-weight:700;color:var(--ink);font-size:10.5px;font-style:normal;margin-top:16px}
.arrow{position:absolute;top:295px;width:24px;height:24px}
.rev-buttons{position:absolute;left:160px;top:530px;width:210px;display:flex;flex-direction:column;gap:10px}
.rev-buttons .btn{text-align:center;border-radius:3px;padding:8px 0}
.rev-buttons .btn.ghost{background:var(--white);color:var(--ink);border:1px solid var(--line)}
.rev-box{position:absolute;top:530px;width:305px;height:135px;border:1px solid var(--line);background:var(--white);text-align:center;padding-top:20px;box-shadow:0 2px 8px rgba(0,0,0,.06)}
.rev-box .mark{font-family:"Montserrat",sans-serif;font-weight:700;font-size:18px;color:var(--ink);display:flex;align-items:center;justify-content:center;gap:8px}
.rev-box .mark i{width:14px;height:14px;border-radius:50%;background:var(--ink);display:inline-block}
.rev-box p{font-size:11px;color:var(--text);margin:12px 40px 8px;line-height:1.45}
.rev-box .more{font-size:9px;font-weight:700;color:var(--olive-dark);text-transform:uppercase}

/* featured destination */
.featured{position:absolute;top:2710px;left:0;width:1200px;height:1000px;background:linear-gradient(180deg,#e9f2f5 0%,#fff 25%)}
.strip{position:absolute;left:160px;top:60px;display:flex;gap:6px}
.thumb{width:104px;height:168px;border-radius:3px;position:relative;box-shadow:0 2px 6px rgba(0,0,0,.2)}
.thumb span{position:absolute;left:0;right:0;bottom:8px;text-align:center;color:var(--white);font-size:9px;font-weight:700;line-height:1.25;text-shadow:0 1px 2px rgba(0,0,0,.5)}
.thumb.active{background:linear-gradient(180deg,#b07a52,#6e4028);transform:translateY(-4px)}
.featured .section-title{position:absolute;top:265px;left:0;width:1200px}
.featured .tag{position:absolute;top:300px;width:1200px;text-align:center;font-size:12px;color:var(--muted)}
.slider{position:absolute;left:160px;top:350px;width:880px;height:330px;border-radius:6px;background:
  radial-gradient(ellipse 180px 200px at 520px 170px,rgba(150,110,80,.7),rgba(150,110,80,0) 75%),
  radial-gradient(ellipse 120px 180px at 240px 190px,rgba(110,80,60,.6),rgba(110,80,60,0) 75%),
  linear-gradient(90deg,#15100c 0%,#3a2618 40%,#22160f 70%,#0e0a08 100%)}
.slider .caption{position:absolute;left:18px;bottom:14px;color:var(--white);font-size:11px;font-weight:600}
.slider .nav-circ{position:absolute;top:150px;width:34px;height:34px;border-radius:50%;background:rgba(0,0,0,.5);display:flex;align-items:center;justify-content:center}
.mini-strip{position:absolute;left:160px;top:696px;display:flex;gap:5px}
.mini-strip div{width:105px;height:62px;border-radius:2px}
.feat-text{position:absolute;left:160px;top:785px;width:880px}
.feat-text h4{font-size:12px;font-weight:700;margin-bottom:6px}
.feat-text p{font-size:11px;line-height:1.6;color:var(--text)}

/* itineraries */
.itins{position:absolute;top:3710px;left:0;width:1200px;height:760px;background:var(--white)}
.itins .section-title{margin-top:60px}
.itin-cards{position:absolute;left:160px;top:205px;display:flex;gap:30px}
.itin{width:273px;height:440px;background:var(--white);border-radius:6px;box-shadow:0 4px 14px rgba(0,0,0,.14);overflow:hidden;position:relative}
.itin .ph{height:170px;background:
  radial-gradient(ellipse 110px 40px at 136px 120px,rgba(236,242,248,.9),rgba(236,242,248,0) 75%),
  linear-gradient(180deg,#3e78b4 0%,#7fb1d8 45%,#8aa2b6 65%,#2e4f6e 100%)}
.itin-body{padding:14px 16px}
.itin h3{font-size:12.5px;font-weight:700;line-height:1.35;margin-bottom:12px}
.itin .row{display:flex;gap:8px;font-size:10px;color:var(--text);margin-bottom:8px;line-height:1.4;padding-right:50px}
.itin .row svg{flex:none;margin-top:1px}
.badge{position:absolute;right:14px;top:346px;width:40px;height:40px;border-radius:50%;background:var(--gold)}
.itin .btn{position:absolute;left:0;right:0;bottom:0;border-radius:0;text-align:center;padding:12px 0}

/* contact */
.contact{position:absolute;top:4470px;left:0;width:1200px;height:370px;background:linear-gradient(180deg,#fff 0%,#fbe98a 45%,#f5c70a 100%)}
.contact h2{position:absolute;left:160px;top:40px;width:500px;font-size:22px;font-weight:800;line-height:1.3;text-transform:uppercase}
.contact p{position:absolute;left:160px;width:440px;font-size:11.5px;line-height:1.55;color:var(--text)}
.contact-form{position:absolute;left:680px;top:30px;width:360px}
.contact-form label{display:block;font-size:10.5px;color:var(--ink);margin:8px 0 5px}
.select{height:32px;background:var(--white);border:1px solid #ddd;border-radius:3px;font-size:10px;color:var(--muted);display:flex;align-items:center;justify-content:space-between;padding:0 12px}
.contact-form .btn{display:block;margin-top:12px;text-align:center;border-radius:3px;padding:11px 0;font-size:11px}

/* footer */
.footer{position:absolute;top:4840px;left:0;width:1200px;height:377px;background:var(--black);color:#cfcfcf}
.foot-brand{position:absolute;left:160px;top:60px;display:flex;flex-direction:column;align-items:center;width:120px;gap:8px}
.foot-brand .dot{width:84px;height:84px;border-radius:50%;background:var(--gold)}
.foot-brand span{font-family:"Montserrat",sans-serif;font-weight:800;font-size:10px;color:var(--gold);text-align:center;text-transform:uppercase;line-height:1.3}
.foot-col{position:absolute;top:60px}
.foot-col h4{color:var(--white);font-size:13px;font-weight:800;text-transform:uppercase;margin-bottom:14px}
.foot-col li{list-style:none;font-size:10.5px;line-height:1.9;white-space:nowrap}
.follow{position:absolute;left:305px;top:225px}
.follow h4{color:var(--white);font-size:13px;font-weight:800;text-transform:uppercase;margin-bottom:10px}
.follow .socials{display:flex;gap:10px}
.follow .socials i{width:16px;height:16px;border-radius:50%;background:#cfcfcf;display:block}
.copy{position:absolute;left:0;bottom:0;width:1200px;height:44px;border-top:1px solid #2a2a2a;display:flex;align-items:center;justify-content:space-between;padding:0 160px;font-size:10px;color:#9a9a9a}
.copy b{color:var(--gold);font-weight:600}
</style>
</head>
<body>

<section class="hero" role="img" aria-label="Panorama of snowy Patagonian peaks above a green valley">
  <header class="topbar">
    <div class="brand"><span class="brand-dot"></span>Velmora Trails &amp; Voyages</div>
    <nav class="nav">
      <a class="active">Home</a><a>Testimonials</a><a>Sample Itineraries</a><a>About Us</a><a>Contact</a>
    </nav>
    <div class="contact-mini">
      <b><svg width="11" height="11" viewBox="0 0 24 24"><path fill="#f2c200" d="M6.6 10.8a15 15 0 0 0 6.6 6.6l2.2-2.2c.3-.3.7-.4 1-.2 1.1.4 2.3.6 3.6.6.6 0 1 .4 1 1V20c0 .6-.4 1-1 1A17 17 0 0 1 3 4c0-.6.4-1 1-1h3.5c.6 0 1 .4 1 1 0 1.3.2 2.5.6 3.6.1.3 0 .7-.2 1z"/></svg>1-888-555-0142</b>
      hello@velmoratrailsandvoyages.example
    </div>
    <span class="btn">Get Your Custom Itinerary</span>
    <span class="lang">EN ▾</span>
  </header>
</section>

<section class="memories">
  <h2 class="section-title">Bring back home the sweetest collection of<br>ever-lasting memories</h2>
  <div class="mem-cards">
    <article class="mem-card hl">
      <div class="mem-icon"></div>
      <h3>Experience the peace of mind of a worry-free tour</h3>
      <p>"Our planners gave us the gift of calm. Every detail was ready before we even asked about it."</p>
      <div class="by">— Hanna Lowe &amp; Family</div>
    </article>
    <article class="mem-card">
      <div class="mem-icon"></div>
      <h3>Unparalleled personalized care 24/7</h3>
      <p>"Your team answered every message fast, day or night, and made the whole trip feel easy."</p>
      <div class="by">— Dana &amp; Nell Carrow</div>
    </article>
    <article class="mem-card">
      <div class="mem-icon"></div>
      <h3>Hand-picked tour guides to guarantee a first-class experience</h3>
      <p>"The local guides were kind, smart and fun. We felt like friends by the end of the week."</p>
      <div class="by">— Gavin &amp; Sofia Emrick</div>
    </article>
    <article class="mem-card">
      <div class="mem-icon"></div>
      <h3>Impressive Trip Reviews From Guests who You Can Contact!</h3>
      <p>"Talk to past guests yourself. Their honest words made us book with full confidence."</p>
      <div class="by">— Joan Smithers</div>
    </article>
  </div>
</section>

<section class="chooser">
  <h2 class="section-title">Choose your destination and get a customized<br>proposal in under 24hs</h2>
  <div class="form-bar">
    <div class="field"><svg width="12" height="12" viewBox="0 0 24 24"><rect x="3" y="5" width="18" height="16" rx="2" fill="none" stroke="#1d1d1d" stroke-width="2"/><path d="M3 10h18" stroke="#1d1d1d" stroke-width="2"/></svg>Trip start date</div>
    <div class="field"><svg width="12" height="12" viewBox="0 0 24 24"><circle cx="12" cy="12" r="9" fill="none" stroke="#1d1d1d" stroke-width="2"/><path d="M12 7v5l3 2" stroke="#1d1d1d" stroke-width="2" fill="none"/></svg>Trip duration</div>
    <div class="field"><svg width="12" height="12" viewBox="0 0 24 24"><path d="M3 18v-6h18v6M3 12V7h8v5" fill="none" stroke="#1d1d1d" stroke-width="2"/></svg>Number of rooms</div>
    <div class="field"><svg width="12" height="12" viewBox="0 0 24 24"><circle cx="12" cy="12" r="9" fill="none" stroke="#1d1d1d" stroke-width="2"/></svg>Looking for?</div>
  </div>
  <span class="btn cta">Get your custom itinerary in under 24hs</span>
  <div class="lake" role="img" aria-label="Turquoise glacial lake with distant mountains"></div>
  <div class="dest-grid">
    <div class="dest"><div class="ph" role="img" aria-label="Astronomical clock tower" style="background:radial-gradient(circle at 50% 45%,#d9b46a 0%,#b0843e 35%,rgba(90,74,56,0) 70%),linear-gradient(160deg,#6a8fb8,#5a4a38)"><span class="info">INFO</span></div><div class="name"><span class="check"><svg width="9" height="9" viewBox="0 0 10 10"><path d="M1 5l3 3 5-6" stroke="#1d1d1d" stroke-width="1.6" fill="none"/></svg></span>Suggest for me</div></div>
    <div class="dest"><div class="ph" role="img" aria-label="Buenos Aires waterfront skyline" style="background:linear-gradient(180deg,#7fa9d4 0%,#b8cbe0 40%,#8b97a6 60%,#4b6178 100%)"><span class="info">INFO</span></div><div class="name">Buenos Aires</div></div>
    <div class="dest"><div class="ph" role="img" aria-label="Iguazu waterfalls in green jungle" style="background:radial-gradient(ellipse 70px 60px at 50% 50%,#f2f4f4,rgba(242,244,244,0) 80%),linear-gradient(180deg,#9fc0dc,#7a9e6a 55%,#476e38)"><span class="info">INFO</span></div><div class="name">Iguazu Falls</div></div>
    <div class="dest"><div class="ph" role="img" aria-label="Tropical beach with turquoise sea" style="background:linear-gradient(180deg,#5aa6dc 0%,#9ad2e6 30%,#2fb8b4 55%,#e8d9a8 75%,#6d8a4e 100%)"><span class="info">INFO</span></div><div class="name">Fernando de Noronha</div></div>
    <div class="dest"><div class="ph" role="img" aria-label="Glacier wall over a lake" style="background:linear-gradient(180deg,#4f86bf 0%,#a9c6df 35%,#e6eff5 55%,#7aa0bc 75%,#3f6a8c 100%)"><span class="info">INFO</span></div><div class="name">El Calafate</div></div>
    <div class="dest"><div class="ph" role="img" aria-label="Cable car over forested mountains" style="background:linear-gradient(180deg,#9fc2e2 0%,#c9dbe8 30%,#6f8f6c 55%,#3e5a3a 100%)"><span class="info">INFO</span></div><div class="name">Bariloche</div></div>
    <div class="dest"><div class="ph" role="img" aria-label="Harbor town beneath snowy peaks" style="background:linear-gradient(180deg,#6f95c4 0%,#dfe7ee 35%,#8a9aaa 55%,#4a5e72 100%)"><span class="info">INFO</span></div><div class="name">Ushuaia</div></div>
    <div class="dest"><div class="ph" role="img" aria-label="Sea lions resting on rocky shore" style="background:radial-gradient(ellipse 80px 50px at 50% 60%,#6e6b66,rgba(110,107,102,0) 80%),linear-gradient(180deg,#aebbc4,#8c8f8a 55%,#4f4b44)"><span class="info">INFO</span></div><div class="name">Peninsula Valdes</div></div>
  </div>
</section>

<section class="reviews">
  <h2 class="section-title">Our guests are raving about us!</h2>
  <p class="subtitle">Read the final reviews of our past guests (and contact any of them if you'd like)</p>
  <svg class="arrow" style="left:128px" viewBox="0 0 24 24"><path d="M15 5l-7 7 7 7" stroke="#555" stroke-width="2.5" fill="none"/></svg>
  <svg class="arrow" style="left:1048px" viewBox="0 0 24 24"><path d="M9 5l7 7-7 7" stroke="#555" stroke-width="2.5" fill="none"/></svg>
  <article class="testi">
    <div class="testi-photo" role="img" aria-label="Family rafting together on a river"></div>
    <div class="testi-body">
      <h4>Ronald &amp; Lila Ashbury and Family<br>(Chapel Hill, North Carolina, United States)</h4>
      <p>"It seemed impossible. Three generations, seven people, 10 days, 4 locations, domestic travel, tours, transfers, and accommodations. All went fine and better than planned."</p>
      <p>"So what happened? Everything was smooth, as promised, with outstanding people and the team was always a step ahead of us."</p>
      <p>"I have never had an experience like this one and I would recommend it to anyone!"</p>
      <p class="visited">Ronald &amp; Lila visited: Buenos Aires, Bariloche, El Calafate and Ushuaia.</p>
    </div>
  </article>
  <div class="rev-buttons">
    <span class="btn">See full testimonial</span>
    <span class="btn ghost">See guest itinerary</span>
    <span class="btn ghost">Contact this guest</span>
    <span class="btn ghost">Get your custom itinerary</span>
  </div>
  <div class="rev-box" style="left:405px">
    <div class="mark"><i></i>TrailReviews</div>
    <p>Read trip reviews our guests have posted on TrailReviews</p>
    <div class="more">Read more ›</div>
  </div>
  <div class="rev-box" style="left:735px">
    <div class="mark">FriendWall</div>
    <p>Read trip reviews our guests have posted on FriendWall</p>
    <div class="more">Read more ›</div>
  </div>
</section>

<section class="featured">
  <div class="strip">
    <div class="thumb active" role="img" aria-label="Buenos Aires street scene"><span>Buenos Aires<br>(City of Tango)</span></div>
    <div class="thumb" role="img" aria-label="Iguazu Falls" style="background:linear-gradient(180deg,#8db4d6,#e6ecec 45%,#5d8a4c)"><span>Iguazu Falls</span></div>
    <div class="thumb" role="img" aria-label="El Calafate glacier" style="background:linear-gradient(180deg,#4f86bf,#c9dbe8 55%,#6d9ac6)"><span>El Calafate</span></div>
    <div class="thumb" role="img" aria-label="Bariloche lakes" style="background:linear-gradient(180deg,#9cbfdf,#6f8f6c 55%,#4f6e4a)"><span>Bariloche</span></div>
    <div class="thumb" role="img" aria-label="Ushuaia bay" style="background:linear-gradient(180deg,#7ea0c8,#d6e0e8 45%,#52657a)"><span>Ushuaia</span></div>
    <div class="thumb" role="img" aria-label="Salta desert hills" style="background:linear-gradient(180deg,#8fb3d6,#c9a27a 45%,#7a5234)"><span>Salta</span></div>
    <div class="thumb" role="img" aria-label="Peninsula Valdes coast" style="background:linear-gradient(180deg,#9bb0be,#8c8f8a 55%,#5e5a52)"><span>Peninsula<br>Valdes (Nature)</span></div>
    <div class="thumb" role="img" aria-label="Patagonian peaks" style="background:linear-gradient(180deg,#88a9cc,#d9e3ea 40%,#3e5566)"><span>El Chalten<br>(The Last<br>Patagonian<br>Frontier)</span></div>
  </div>
  <h2 class="section-title">Featured destination: Buenos Aires</h2>
  <div class="tag">(The City of Tango)</div>
  <div class="slider" role="img" aria-label="Tango dancers performing on a dim stage with musicians">
    <div class="nav-circ" style="left:16px"><svg width="14" height="14" viewBox="0 0 24 24"><path d="M15 5l-7 7 7 7" stroke="#fff" stroke-width="3" fill="none"/></svg></div>
    <div class="nav-circ" style="right:16px"><svg width="14" height="14" viewBox="0 0 24 24"><path d="M9 5l7 7-7 7" stroke="#fff" stroke-width="3" fill="none"/></svg></div>
    <div class="caption">Experience an evening of charm and sensuality at one of the best Tango venues in Buenos Aires</div>
  </div>
  <div class="mini-strip" role="img" aria-label="Row of small Buenos Aires photos">
    <div style="background:linear-gradient(180deg,#5a3f30,#2a1d16)"></div><div style="background:linear-gradient(180deg,#a9bfd6,#6e7f96)"></div><div style="background:linear-gradient(180deg,#c79a6c,#8a6240)"></div><div style="background:linear-gradient(180deg,#7fa0c4,#4a6a8c)"></div><div style="background:linear-gradient(180deg,#e2cfa6,#b09670)"></div><div style="background:linear-gradient(180deg,#9cbf86,#5a7a48)"></div><div style="background:linear-gradient(180deg,#5f7590,#2f3f56)"></div><div style="background:linear-gradient(180deg,#b3c6da,#7890ad)"></div>
  </div>
  <div class="feat-text">
    <h4>Buenos Aires (City of Tango):</h4>
    <p>It's the birthplace and capital of tango, and now the stylish modern capital of a nation. Buenos Aires is a sensual and captivating city with an eclectic, elegant and distinguished collection of architecture, delectable first-class cuisine, and plenty of fascinating cultural highlights to enjoy. It's home to some of the most important museums of Latin America and to the finest tango musicians, dancers and singers, all of whom you can see perform in the city's top tango venues.</p>
  </div>
</section>

<section class="itins">
  <h2 class="section-title">See our sample itineraries</h2>
  <p class="subtitle">If you are looking for a first-class Argentina Travel Experience see our Suggested<br>Argentina Travel Packages Below!</p>
  <div class="itin-cards">
    <article class="itin">
      <div class="ph" role="img" aria-label="Glacier peaks under blue sky"></div>
      <div class="itin-body">
        <h3>An Exclusive Adventure at the Scenic Patagonia Region and the Mighty Iguazu Falls</h3>
        <div class="row"><svg width="12" height="12" viewBox="0 0 24 24"><circle cx="12" cy="12" r="9" fill="none" stroke="#8da51c" stroke-width="2"/><path d="M12 7v5l3 2" stroke="#8da51c" stroke-width="2" fill="none"/></svg>Trip duration: 14 days / 13 nights</div>
        <div class="row"><svg width="12" height="12" viewBox="0 0 24 24"><path d="M12 2a7 7 0 0 0-7 7c0 5 7 13 7 13s7-8 7-13a7 7 0 0 0-7-7z" fill="#8da51c"/></svg><span>5 destinations visited:<br>Buenos Aires, Iguazu Falls, Bariloche, El Calafate and Ushuaia</span></div>
        <div class="row"><svg width="12" height="12" viewBox="0 0 24 24"><path d="M4 12l5 5L20 6" stroke="#8da51c" stroke-width="3" fill="none"/></svg>12 first-class tours included</div>
      </div>
      <span class="badge"></span>
      <span class="btn">See itinerary details</span>
    </article>
    <article class="itin">
      <div class="ph" role="img" aria-label="Glacier peaks under blue sky"></div>
      <div class="itin-body">
        <h3>A Discovery Journey to the Ends of the Earth, the Patagonian Glaciers, and the Mighty Iguazu Falls</h3>
        <div class="row"><svg width="12" height="12" viewBox="0 0 24 24"><circle cx="12" cy="12" r="9" fill="none" stroke="#8da51c" stroke-width="2"/><path d="M12 7v5l3 2" stroke="#8da51c" stroke-width="2" fill="none"/></svg>Trip duration: 11 days / 10 nights</div>
        <div class="row"><svg width="12" height="12" viewBox="0 0 24 24"><path d="M12 2a7 7 0 0 0-7 7c0 5 7 13 7 13s7-8 7-13a7 7 0 0 0-7-7z" fill="#8da51c"/></svg><span>4 destinations visited:<br>Buenos Aires, Iguazu Falls, El Calafate and Ushuaia</span></div>
        <div class="row"><svg width="12" height="12" viewBox="0 0 24 24"><path d="M4 12l5 5L20 6" stroke="#8da51c" stroke-width="3" fill="none"/></svg>10 first-class tours included</div>
      </div>
      <span class="badge"></span>
      <span class="btn">See itinerary details</span>
    </article>
    <article class="itin">
      <div class="ph" role="img" aria-label="Glacier peaks under blue sky"></div>
      <div class="itin-body">
        <h3>An Exclusive Journey to the Patagonian Glaciers, the Mighty Iguazu Falls and the City of Tango</h3>
        <div class="row"><svg width="12" height="12" viewBox="0 0 24 24"><circle cx="12" cy="12" r="9" fill="none" stroke="#8da51c" stroke-width="2"/><path d="M12 7v5l3 2" stroke="#8da51c" stroke-width="2" fill="none"/></svg>Trip duration: 9 days / 8 nights</div>
        <div class="row"><svg width="12" height="12" viewBox="0 0 24 24"><path d="M12 2a7 7 0 0 0-7 7c0 5 7 13 7 13s7-8 7-13a7 7 0 0 0-7-7z" fill="#8da51c"/></svg><span>3 destinations visited:<br>Buenos Aires, Iguazu Falls and El Calafate</span></div>
        <div class="row"><svg width="12" height="12" viewBox="0 0 24 24"><path d="M4 12l5 5L20 6" stroke="#8da51c" stroke-width="3" fill="none"/></svg>8 first-class tours included</div>
      </div>
      <span class="badge"></span>
      <span class="btn">See itinerary details</span>
    </article>
  </div>
</section>

<section class="contact">
  <h2>Contact any of 150+ past guests<br>from the United States</h2>
  <p style="top:120px">No other company will offer you a list of over one hundred past guests who you can choose from to contact directly.</p>
  <p style="top:168px">Our guests have had superb travel experiences; contact them and check out firsthand what they have to say about our attention to detail and first-class service.</p>
  <div class="contact-form">
    <label>Select the type of guests you're interested in contacting</label>
    <div class="select">Select Type <span>▾</span></div>
    <label>Destinations visited by the Guest</label>
    <div class="select">Select an option <span>▾</span></div>
    <span class="btn">Search</span>
  </div>
</section>

<footer class="footer">
  <div class="foot-brand"><div class="dot"></div><span>Velmora Trails<br>&amp; Voyages</span></div>
  <div class="foot-col" style="left:305px">
    <h4>Vacation Types</h4>
    <ul><li>Argentina Honeymoon</li><li>Argentina Family Vacation</li><li>Argentina Luxury Tours</li><li>Customized Trips to Argentina</li><li>Argentina Travel Packages</li></ul>
  </div>
  <div class="follow">
    <h4>Follow Us</h4>
    <div class="socials"><i></i><i></i><i></i></div>
  </div>
  <div class="foot-col" style="left:545px">
    <h4>Destinations</h4>
    <ul><li>Iguazu Falls Tours &amp; Travel Package</li><li>El Calafate Tours &amp; Travel Package</li><li>Buenos Aires Tours &amp; Travel Package</li><li>Ushuaia Tours &amp; Travel Package</li><li>Bariloche Tours &amp; Travel Package</li><li>Peninsula Valdes Tours &amp; Travel Package</li><li>Patagonia Tours &amp; Travel Package</li></ul>
  </div>
  <div class="foot-col" style="left:850px">
    <h4>Velmora Voyages</h4>
    <ul><li>Home</li><li>About Us</li><li>Contact Us</li><li>Useful Info</li><li>Privacy Policy</li><li>Terms &amp; Conditions</li><li>Sitemap</li></ul>
  </div>
  <div class="copy"><span><b>© Velmora Trails &amp; Voyages</b> 2016 · All Rights Reserved</span><span>Design by Velmora Studio</span></div>
</footer>

</body>
</html>
```